Construction Company Business Card

Business Card Design using new Logo

Contact Information for Business Card

include all company info and website

Requirements
Must have
• Wesley Corman - President
ph. 254-617-0382
Cedar Knoll, TX
wesley@ironmarkframing.com
www.ironmarkframing.com

```html
<!DOCTYPE html>
<html lang="en">
<head>
<meta charset="utf-8">
<title>Ironmark Framing – Business Card</title>
<link href="https://fonts.googleapis.com/css2?family=Raleway:wght@400;500;700&family=Arimo:wght@400;700&display=swap" rel="stylesheet">
<style>
  :root {
    --brand-red: #c02026;
    --brand-grey: #b9b8bd;
    --ink: #4a4a4a;
    --rule: #9a9a9a;
    --paper: #ffffff;
    --backdrop: #e6e6e6;
  }
  * { box-sizing: border-box; margin: 0; padding: 0; }
  html, body { width: 1200px; height: 1200px; overflow: hidden; }
  body {
    background: var(--backdrop);
    position: relative;
    font-family: "Arimo", Arial, sans-serif;
  }
  .card {
    position: absolute;
    top: 303px;
    width: 369px;
    height: 594px;
    overflow: hidden;
  }
  .card--front { left: 216px; background: var(--brand-grey); }
  .card--back { left: 615px; background: var(--paper); }

  /* Front */
  .front__band {
    position: absolute; top: 0; left: 0; right: 0;
    height: 264px;
    background: var(--brand-red);
  }
  .front__name {
    position: absolute; top: 268px; left: 0; right: 0;
    text-align: center;
    font-family: "Raleway", sans-serif;
    font-weight: 500;
    font-size: 27px;
    letter-spacing: 2px;
    color: var(--paper);
  }
  .front__web {
    position: absolute; top: 540px; left: 0; right: 0;
    text-align: center;
    font-family: "Arimo", sans-serif;
    font-weight: 700;
    font-size: 16px;
    letter-spacing: 2.6px;
    color: var(--brand-red);
  }

  /* Back */
  .back__brand {
    position: absolute; top: 160px; left: 0; right: 0;
    display: flex; justify-content: center; align-items: center; gap: 8px;
  }
  .back__brand-mark { width: 14px; height: 14px; background: var(--brand-red); }
  .back__brand-name {
    font-family: "Raleway", sans-serif;
    font-weight: 500;
    font-size: 23px;
    letter-spacing: 1.5px;
    color: var(--brand-grey);
  }
  .back__person {
    position: absolute; top: 333px; left: 0; right: 0; text-align: center;
  }
  .back__person-name {
    font-family: "Raleway", sans-serif;
    font-weight: 700;
    font-size: 21px;
    color: var(--brand-red);
    line-height: 1.1;
  }
  .back__person-title {
    font-family: "Raleway", sans-serif;
    font-weight: 500;
    font-size: 16px;
    color: var(--ink);
    margin-top: 4px;
  }
  .divider {
    position: absolute; left: 0; right: 0;
    display: flex; justify-content: center; align-items: center; gap: 4px;
  }
  .divider__rule { width: 52px; height: 1px; background: var(--rule); margin: 0 2px; }
  .divider--icons { top: 395px; }
  .divider--pin { top: 500px; }
  .divider--pin .divider__rule { width: 75px; margin: 0 6px; }
  .icon { width: 25px; height: 25px; display: block; }
  .back__contact {
    position: absolute; top: 428px; left: 0; right: 0;
    text-align: center;
    font-size: 17px;
    line-height: 21.5px;
    color: var(--ink);
  }
  .back__location {
    position: absolute; top: 532px; left: 0; right: 0;
    text-align: center;
    font-size: 17px;
    color: var(--ink);
  }
</style>
</head>
<body>

<section class="card card--front" aria-label="Business card front">
  <div class="front__band"></div>
  <div class="front__name">IRONMARK FRAMING</div>
  <div class="front__web">www.ironmarkframing.com</div>
</section>

<section class="card card--back" aria-label="Business card back">
  <div class="back__brand">
    <span class="back__brand-mark"></span>
    <span class="back__brand-name">IRONMARK FRAMING</span>
  </div>

  <div class="back__person">
    <div class="back__person-name">WESLEY CORMAN</div>
    <div class="back__person-title">President</div>
  </div>

  <div class="divider divider--icons">
    <span class="divider__rule"></span>
    <svg class="icon" viewBox="0 0 25 25" aria-label="Phone">
      <rect width="25" height="25" rx="3" fill="var(--brand-red)"/>
      <path d="M5 10c0-3 15-3 15 0v1.5h-4V10H9v1.5H5z" fill="#fff"/>
      <rect x="7" y="12" width="11" height="7" rx="1.5" fill="#fff"/>
    </svg>
    <svg class="icon" viewBox="0 0 25 25" aria-label="Email">
      <rect width="25" height="25" rx="3" fill="var(--brand-red)"/>
      <rect x="5.5" y="8" width="14" height="10" fill="none" stroke="#fff" stroke-width="1.4"/>
      <path d="M5.5 8l7 6 7-6M5.5 18l5-4.5M19.5 18l-5-4.5" fill="none" stroke="#fff" stroke-width="1.2"/>
    </svg>
    <svg class="icon" viewBox="0 0 25 25" aria-label="Website">
      <rect width="25" height="25" rx="3" fill="var(--brand-red)"/>
      <circle cx="12.5" cy="12.5" r="7" fill="#fff"/>
      <path d="M9 9c2 0 3 1 2.5 2.5S9 13 9.5 15M14 7.5c0 2 2 2 3 3.5M14.5 15c1-1 2.5-1 3-.5" fill="none" stroke="var(--brand-red)" stroke-width="1.5"/>
    </svg>
    <span class="divider__rule"></span>
  </div>

  <div class="back__contact">
    <div>254-617-0382</div>
    <div>wesley@ironmarkframing.com</div>
    <div>www.ironmarkframing.com</div>
  </div>

  <div class="divider divider--pin">
    <span class="divider__rule"></span>
    <svg class="icon" viewBox="0 0 25 25" aria-label="Location">
      <rect width="25" height="25" rx="3" fill="var(--brand-red)"/>
      <path d="M12.5 20c-3-4-5-6.5-5-9a5 5 0 0 1 10 0c0 2.5-2 5-5 9z" fill="#fff"/>
      <circle cx="12.5" cy="11" r="1.8" fill="var(--brand-red)"/>
    </svg>
    <span class="divider__rule"></span>
  </div>

  <div class="back__location">Cedar Knoll, TX</div>
</section>

</body>
</html>
```